Business card for Tolvery Anesthesia LLC

This is for a business care for Tolvery Anesthesia LLC. Dr. Lisbeth Tolvery, CRNA, DNAP is the sole provider in the LLC. Business address is 4718 N Brackley Street,
Oakhaven, PA 17342
CRNA stands for certified registered nurse anesthetist
"Keeping you safe and comfortable"
I plan to give this business card to the patients that I provide anesthesia to.
Creative design that ties into Anesthesia. Calm soothing colors.

Target Market(s)

Business card for my patients.

Industry/Entity Type

Medicine

Contact Information for Business Card

Creative, professional, eye catching

Logo Text

Tolvery Anesthesia

Font styles to use
Serif
Script

Colors

Designer to choose colors to be used in the design.

Requirements
Must have
• Tolvery Anesthesia
• Dr. Lisbeth Tolvery, CRNA, DNAP
• tolvery.anesthesia@ quillmail.net
Nice to have
• "Keeping you safe and comfortable"
Should not have
• phone number

```html
<!DOCTYPE html>
<html lang="en">
<head>
<meta charset="utf-8">
<title>Tolvery Anesthesia LLC – Business Card</title>
<link rel="stylesheet" href="https://fonts.googleapis.com/css2?family=Source+Sans+3:wght@400;600&family=Sniglet:wght@800&display=swap">
<style>
  :root {
    --backdrop: #1d1d1d;
    --card-blue: #0a55a8;
    --card-green: #22b14c;
    --ink-white: #ffffff;
    --soft-white: rgba(255, 255, 255, 0.85);
    --soft-fade: rgba(255, 255, 255, 0);
  }
  html, body {
    margin: 0;
    width: 1200px;
    height: 901px;
    overflow: hidden;
    background: var(--backdrop);
  }
  .stage {
    width: 1200px;
    height: 901px;
    display: flex;
    align-items: center;
    justify-content: center;
  }
  .business-card {
    position: relative;
    width: 840px;
    height: 480px;
    background: var(--card-blue);
    overflow: hidden;
    font-family: "Source Sans 3", sans-serif;
    color: var(--ink-white);
  }
  .card-bands {
    position: absolute;
    inset: 0;
  }
  .patient-illustration {
    position: absolute;
    left: 60px;
    top: 225px;
    width: 190px;
    height: 115px;
    background: radial-gradient(ellipse 50% 60% at 50% 70%, var(--soft-white), var(--soft-fade));
  }
  .company-name {
    position: absolute;
    left: 60px;
    top: 170px;
    margin: 0;
    font-size: 28px;
    font-weight: 400;
    letter-spacing: 0.3px;
  }
  .provider-details {
    position: absolute;
    left: 470px;
    top: 118px;
    margin: 0;
    font-style: normal;
    line-height: 1.15;
  }
  .provider-name {
    display: block;
    font-size: 25px;
    font-weight: 400;
  }
  .provider-credentials {
    font-size: 13px;
  }
  .credential-note {
    display: block;
    font-size: 12.5px;
    margin-bottom: 10px;
  }
  .contact-line {
    display: block;
    font-size: 21px;
  }
  .tagline {
    position: absolute;
    left: 60px;
    right: 60px;
    top: 378px;
    margin: 0;
    text-align: center;
    font-family: "Sniglet", cursive;
    font-weight: 800;
    font-size: 31px;
    letter-spacing: 0.3px;
    white-space: nowrap;
  }
</style>
</head>
<body>
<main class="stage">
  <article class="business-card">
    <svg class="card-bands" width="840" height="480" viewBox="0 0 840 480" aria-hidden="true">
      <path d="M0 340 H250 L268 300 L282 240 L296 345 L310 300 H840 V480 H0 Z" fill="var(--card-green)"/>
      <path d="M248 340 L268 300 L282 240 L296 345 L310 300 H840" fill="none" stroke="var(--ink-white)" stroke-width="7" stroke-linejoin="round"/>
    </svg>

    <div class="patient-illustration" role="img" aria-label="Illustration of a resting patient wearing an anesthesia mask"></div>

    <h1 class="company-name">Tolvery Anesthesia LLC</h1>

    <address class="provider-details">
      <span class="provider-name">Dr. Lisbeth Tolvery, <span class="provider-credentials">CRNA, DNAP</span></span>
      <span class="credential-note">CRNA stands for certified registered nurse anesthetist</span>
      <span class="contact-line">4718 N Brackley Street,</span>
      <span class="contact-line">Oakhaven, PA 17342</span>
      <span class="contact-line">tolvery.anesthesia@ quillmail.net</span>
    </address>

    <p class="tagline">" Keeping you safe and comfortable"</p>
  </article>
</main>
</body>
</html>
```